Bespoke Branding Agency "Cobalt Kite" seeks uplifting wordpress site

Looking for a SIMPLE, CLEAN, easy to manage wordpress site for our start-up Branding business. Our company is "Cobalt Kite" and the site should reflect our vision.

We formed the company after making the decision never to work the average 9 to 5 work life again. We have vowed to never work in traditional corporate culture again. We are committed to a happier life with reduced stress and increased job satisfaction.

We want to build brands that make people happy.

We want to work with people who believe that you don’t have to be an asshole to be successful.

We believe that success should not be measured in monetary terms, but rather in happiness scores.

We believe in the Dorian Pellsworth song lyric "Rivers carry quiet tunes”.

We love sunflowers.

We prefer brevity over long wind.

We are motivated by creativity not money.

We love spending time with friends and family, and see this as our main priority in life.

We know life is short.

```html
<!DOCTYPE html>
<html lang="en">
<head>
<meta charset="utf-8">
<title>Cobalt Kite — Branding Agency</title>
<link href="https://fonts.googleapis.com/css2?family=Open+Sans:wght@300;400;600;700;800&display=swap" rel="stylesheet">
<style>
  :root {
    --brand-orange: #f6a712;
    --cta-orange: #f37021;
    --ink: #2b2b2b;
    --body-ink: #3a3a2a;
    --footer-ink: #555555;
    --white: #ffffff;
    --sky-teal: #6cb8a6;
    --pale-sun: #f3f3b0;
    --sun-yellow: #f2e64a;
    --warm-gold: #e8b92c;
  }
  * { box-sizing: border-box; margin: 0; padding: 0; }
  html, body { width: 1200px; height: 731px; overflow: hidden; }
  body { font-family: "Open Sans", Arial, sans-serif; background: var(--white); position: relative; }

  .hero { position: absolute; left: 0; top: 0; width: 1200px; height: 643px; overflow: hidden; }
  .hero-photo {
    position: absolute; inset: 0;
    background: linear-gradient(135deg, var(--sky-teal) 0%, var(--pale-sun) 30%, var(--sun-yellow) 60%, var(--warm-gold) 100%);
  }

  .logo {
    position: absolute; left: 103px; top: 29px; width: 142px; height: 142px;
    border-radius: 50%; background: var(--brand-orange);
    display: flex; flex-direction: column; align-items: center; justify-content: center;
    color: var(--white); font-weight: 700; font-size: 21px; line-height: 1.05; letter-spacing: 2px;
  }

  .main-nav { position: absolute; top: 61px; left: 513px; display: flex; align-items: center; }
  .main-nav a {
    color: var(--ink); text-decoration: none; font-weight: 700; font-size: 15.5px;
    height: 35px; line-height: 35px; white-space: nowrap;
  }
  .main-nav .is-active {
    background: var(--brand-orange); color: var(--white);
    width: 106px; text-align: center; border-radius: 18px;
  }
  .nav-about { margin-left: 30px; }
  .nav-services, .nav-brands, .nav-contact { margin-left: 60px; }

  .hero-copy { position: absolute; left: 98px; top: 238px; width: 540px; }
  .headline { font-weight: 300; font-size: 53px; line-height: 61px; color: var(--ink); letter-spacing: -0.5px; }
  .headline strong { display: block; font-weight: 800; color: var(--brand-orange); letter-spacing: 0; }
  .intro { margin-top: 8px; width: 522px; font-size: 11.2px; line-height: 23px; color: var(--body-ink); }
  .cta {
    display: inline-block; margin-top: 12px; width: 181px; height: 46px; line-height: 46px;
    border-radius: 23px; background: var(--cta-orange); color: var(--white);
    text-align: center; font-weight: 700; font-size: 15.5px; text-decoration: none;
  }

  .slider-dots { position: absolute; left: 1118px; top: 274px; list-style: none; }
  .slider-dots li { width: 8px; height: 8px; border-radius: 50%; background: var(--white); margin-bottom: 17px; }
  .slider-dots li.is-current { background: transparent; border: 1.5px solid rgba(255,255,255,0.85); }

  .site-footer { position: absolute; left: 0; top: 643px; width: 1200px; height: 88px; background: var(--white); }
  .copyright { position: absolute; left: 100px; top: 34px; font-size: 11.5px; color: var(--footer-ink); }
  .follow { position: absolute; left: 898px; top: 35px; font-size: 11px; color: var(--footer-ink); display: flex; gap: 9px; }
  .follow span { white-space: nowrap; }
  .follow .network { color: var(--ink); font-weight: 600; font-size: 10.5px; }
  .follow .label { margin-right: 6px; }
</style>
</head>
<body>
  <section class="hero">
    <div class="hero-photo" role="img" aria-label="Photograph of sunflowers in a sunlit field with rays of light"></div>

    <div class="logo"><span>COBALT</span><span>KITE</span></div>

    <nav class="main-nav">
      <a href="#" class="is-active">Home</a>
      <a href="#" class="nav-about">About Us</a>
      <a href="#" class="nav-services">Services</a>
      <a href="#" class="nav-brands">Brands</a>
      <a href="#" class="nav-contact">Contact Us</a>
    </nav>

    <div class="hero-copy">
      <h1 class="headline">RIVERS CARRY <strong>QUIET TUNES</strong></h1>
      <p class="intro">Lorem Ipsum is simply dummy text of the printing and typesetting industry. Lorem Ipsum has been the industry's standard dummy text ever since the 1500s, when an unknown printer took a galley of type and scrambled it to make a type specimen book.</p>
      <a href="#" class="cta">CLICK HERE</a>
    </div>

    <ul class="slider-dots">
      <li class="is-current"></li><li></li><li></li><li></li><li></li>
    </ul>
  </section>

  <footer class="site-footer">
    <p class="copyright">© Copyrights.2015. Cobalt Kite. All rights reserved.</p>
    <div class="follow">
      <span class="label">Follow Us :</span>
      <span class="network">Fenn</span>
      <span class="network">Wren</span>
      <span class="network">Loom</span>
      <span class="network">Tack</span>
    </div>
  </footer>
</body>
</html>
```